Gaming Headset Packaging Design

We would like a gaming window box style packaging design for our gaming headset.

We want to use the packaging for 2-3 of our gaming headphone series and hence we would not like to put any product pictures on the packaging.

Size: (enclosed die-cut drawing) please feel free to modify the shape of the window
Material: E Flute Paper box
Type: Window Box style
Design features we prefer: gaming, playful, creative, trendy, High tech.
Requirement: AI file is preferred

Enclosed are a detailed description along with competitor designs and existing die-cut drawing (AI format) for your reference.

Any further questions, please feel free to ask.

```html
<!DOCTYPE html>
<html lang="en">
<head>
<meta charset="utf-8">
<title>Pro Gaming Headset 7.1 – Window Box Dieline</title>
<link rel="stylesheet" href="https://fonts.googleapis.com/css2?family=Bungee&family=Oswald:wght@500&family=Roboto+Condensed:wght@400;700&family=Open+Sans:wght@700&display=swap">
<style>
  :root {
    --navy: #04222f;
    --lime: #b5d334;
    --cyan: #29a8e0;
    --sky: #1fb4ef;
    --white: #ffffff;
    --ink: #1f2a1a;
    --paper: #ffffff;
  }
  html, body { margin: 0; padding: 0; overflow: hidden; background: var(--paper); }
  .canvas { width: 1200px; height: 900px; display: block; }
  .title-main { font-family: "Bungee", "Arial Black", sans-serif; fill: var(--navy); }
  .title-pro { font-family: "Bungee", "Arial Black", sans-serif; fill: var(--white); }
  .title-sub { font-family: "Bungee", "Arial Black", sans-serif; fill: var(--navy); }
  .features-head { font-family: "Bungee", "Arial Black", sans-serif; fill: var(--lime); }
  .feature-item { font-family: "Oswald", "Arial Narrow", sans-serif; font-weight: 500; fill: var(--white); font-size: 13.5px; letter-spacing: 0.3px; }
  .spec-text { font-family: "Roboto Condensed", "Arial Narrow", sans-serif; fill: var(--ink); font-size: 5.2px; }
  .spec-head { font-weight: 700; }
  .cut-line { fill: none; stroke: var(--cyan); stroke-width: 0.8; }
  .fold-line { fill: none; stroke: var(--cyan); stroke-width: 0.6; stroke-dasharray: 3 2; }
  .swatch-label { font-family: "Open Sans", Arial, sans-serif; font-weight: 700; font-size: 11px; fill: var(--ink); }
</style>
</head>
<body>
<svg class="canvas" viewBox="0 0 1200 900" xmlns="http://www.w3.org/2000/svg">
  <defs>
    <radialGradient id="halftone-left" cx="0.2" cy="0.8" r="0.9">
      <stop offset="0" stop-color="#1fb4ef" stop-opacity="0.95"/>
      <stop offset="0.55" stop-color="#1784b8" stop-opacity="0.6"/>
      <stop offset="1" stop-color="#04222f" stop-opacity="0"/>
    </radialGradient>
    <linearGradient id="halftone-band" x1="0" y1="0" x2="1" y2="0">
      <stop offset="0" stop-color="#1fb4ef" stop-opacity="0"/>
      <stop offset="0.6" stop-color="#1784b8" stop-opacity="0.6"/>
      <stop offset="1" stop-color="#1fb4ef" stop-opacity="1"/>
    </linearGradient>
    <g id="product-title">
      <text class="title-pro" transform="translate(252 372) rotate(-90)" font-size="11" textLength="34" lengthAdjust="spacingAndGlyphs">PRO</text>
      <text class="title-main" x="258" y="372" font-size="40" textLength="152" lengthAdjust="spacingAndGlyphs">GAMING</text>
      <text class="title-main" x="237" y="403" font-size="33" textLength="176" lengthAdjust="spacingAndGlyphs">HEADSET 7.1</text>
      <text class="title-sub" x="238" y="418" font-size="11.5" textLength="173" lengthAdjust="spacingAndGlyphs">VIRTUAL 7.1 SURROUND SOUND</text>
    </g>
    <g id="tick-icon">
      <circle r="8" fill="var(--lime)"/>
      <circle r="6" fill="var(--navy)"/>
      <path d="M-3.5 0 L-1 3 L4.5 -4" fill="none" stroke="var(--white)" stroke-width="2"/>
    </g>
  </defs>

  <!-- top tuck flap -->
  <path class="cut-line" d="M222 75 L228 75 L228 45 Q228 30 243 30 L570 30 Q585 30 585 45 L585 75"/>
  <path class="cut-line" d="M370 75 L370 78 L440 78 L440 75"/>
  <rect class="top-panel" x="222" y="75" width="364" height="195" fill="var(--lime)"/>
  <use href="#product-title" transform="translate(0 -159)"/>

  <!-- side dust flaps -->
  <path class="cut-line" d="M222 270 L60 260 L35 230 L33 160 L222 160 Z"/>
  <path class="cut-line" d="M590 270 L590 160 L752 160 L778 260 L778 270"/>
  <path class="cut-line" d="M928 270 L928 245 Q928 235 938 235 L988 235 Q998 235 998 245 L998 270"/>

  <!-- main body -->
  <rect class="body" x="30" y="270" width="1113" height="435" fill="var(--navy)"/>
  <rect class="halftone-band" x="760" y="270" width="383" height="48" fill="url(#halftone-band)" role="img" aria-label="Blue halftone dot texture"/>
  <rect class="accent-line" x="30" y="318" width="1113" height="2.5" fill="var(--lime)"/>

  <!-- glue flap -->
  <path class="cut-line" d="M1143 270 L1185 285 L1185 690 L1143 705"/>

  <!-- title bands -->
  <rect class="title-band" x="30" y="325" width="192" height="103" fill="var(--lime)"/>
  <path class="title-band" d="M222 325 L502 325 L445 428 L222 428 Z" fill="var(--lime)"/>
  <rect class="accent-line" x="30" y="430" width="420" height="2.5" fill="var(--lime)"/>
  <use href="#product-title" transform="translate(-200 0)"/>
  <use href="#product-title"/>

  <!-- left panel halftone -->
  <path class="halftone-area" d="M30 432 L222 432 L222 705 L222 730 L150 800 L150 845 L30 845 Z" fill="url(#halftone-left)" role="img" aria-label="Blue halftone dots with faint circular arrow graphic"/>

  <!-- window -->
  <polygon class="window" fill="var(--white)" points="445,342 462,325 655,325 665,335 852,325 888,361 888,433 878,445 878,650 890,662 658,662 648,652 445,662 445,590 458,578 458,492 445,480"/>

  <!-- back panel -->
  <path class="back-panel" d="M858 325 L1143 325 L1143 705 L943 705 L895 655 L895 442 L880 430 L890 362 Z" fill="var(--lime)"/>
  <use href="#product-title" transform="translate(668 0)"/>
  <rect x="895" y="428" width="248" height="2" fill="var(--navy)"/>

  <!-- features -->
  <text class="features-head" x="238" y="483" font-size="16" textLength="148" lengthAdjust="spacingAndGlyphs">HEADSET FEATURES:</text>
  <use href="#tick-icon" x="249" y="504"/>
  <text class="feature-item" x="266" y="509">VIRTUAL 7.1 SURROUND SOUND</text>
  <use href="#tick-icon" x="249" y="533"/>
  <text class="feature-item" x="266" y="538">DUAL DRIVERS ON EACH EAR</text>
  <text class="feature-item" x="266" y="555">FOR ACCURACY</text>
  <use href="#tick-icon" x="249" y="579"/>
  <text class="feature-item" x="266" y="584">3D SOUND VIBRATION</text>
  <use href="#tick-icon" x="249" y="608"/>
  <text class="feature-item" x="266" y="613">BENDABLE STAINLESS-STEEL</text>
  <text class="feature-item" x="266" y="630">HEADBAND</text>
  <use href="#tick-icon" x="249" y="654"/>
  <text class="feature-item" x="266" y="659">SOFT AND SOOTHING EARPADS</text>

  <!-- specifications -->
  <line x1="1010" y1="435" x2="1010" y2="516" stroke="var(--ink)" stroke-width="0.5"/>
  <g class="spec-text">
    <text x="913" y="442" class="spec-head">Headphone Specification:</text>
    <text x="913" y="457">Speaker Diameter: Φ40mm</text>
    <text x="913" y="465.5">Impedance: 32Ω ± 15%</text>
    <text x="913" y="474">Sensitivity S.P.L: 113dB ± 3dB</text>
    <text x="913" y="482.5">Rated Power: 20mW</text>
    <text x="913" y="491">Aggregate capability: 30mW</text>
    <text x="913" y="499.5">Frequency Response: 20-20kHz</text>
    <text x="913" y="508">Plug Type: 3.5mm Stereo</text>
    <text x="1017" y="442" class="spec-head">Microphone Specification:</text>
    <text x="1017" y="457">Microphone Unit: Φ6 x 5mm</text>
    <text x="1017" y="465.5">Sensitivity S.P.L: -38dB ± 3dB</text>
    <text x="1017" y="474">Impedance: &lt;2.2k</text>
    <text x="1017" y="482.5">Frequency Response: 30-16kHz</text>
    <text x="1017" y="491">Standard Operating Voltage: 4.5V</text>
    <text x="1017" y="499.5">S/N Ratio: ≥ 60dB</text>
    <text x="1017" y="508">Plug Type: 3.5mm Stereo</text>
    <text x="906" y="537">Warning: Adjust headphone sound to a proper volume. Loud sound may damage your ears.</text>
    <text x="906" y="545">For traffic safety never use the headset while driving.</text>
    <text x="906" y="558">Caution: If the user attempts to inspect or modify the product in any way we can't guarantee the performance</text>
    <text x="906" y="566">of the product. Specifications and design are subject to possible modification without notice due to improvements.</text>
  </g>
  <rect x="905" y="580" width="226" height="80" fill="none" stroke="var(--ink)" stroke-width="0.6"/>
  <path d="M913 596 V587 H923 M1003 587 H1013 V596 M913 645 V654 H923 M1013 645 V654 H1003" fill="none" stroke="var(--ink)" stroke-width="0.6"/>

  <!-- bottom flaps -->
  <path class="bottom-flap" fill="var(--navy)" d="M230 705 L585 705 L585 765 L522 765 L522 835 Q522 845 512 845 L510 845 L500 835 L500 805 L320 805 L310 815 L310 845 L240 845 Q230 845 230 835 Z"/>
  <path class="bottom-flap" fill="var(--navy)" d="M590 705 L778 705 L778 720 L708 790 L708 845 L695 845 Q685 845 685 835 L685 795 L590 705 Z"/>
  <path class="bottom-flap" fill="var(--navy)" d="M778 705 L1143 705 L1143 712 L1057 800 L1057 835 Q1057 845 1047 845 L878 845 Q868 845 868 835 L868 800 Z"/>
  <path class="halftone-area" d="M230 705 L400 705 L400 805 L320 805 L310 815 L310 845 L240 845 Q230 845 230 835 Z" fill="url(#halftone-left)" opacity="0.5" role="img" aria-label="Blue halftone dot texture"/>
  <path class="cut-line" d="M30 705 L30 845 L150 845 L150 800 L222 730 L222 705"/>

  <!-- fold lines -->
  <g class="fold-line">
    <line x1="222" y1="75" x2="222" y2="705"/>
    <line x1="586" y1="75" x2="586" y2="705"/>
    <line x1="778" y1="270" x2="778" y2="705"/>
    <line x1="1143" y1="270" x2="1143" y2="705"/>
    <line x1="30" y1="270" x2="1143" y2="270"/>
    <line x1="30" y1="705" x2="1143" y2="705"/>
    <line x1="222" y1="75" x2="586" y2="75"/>
  </g>

  <!-- inside shelf colour swatch -->
  <rect x="1003" y="157" width="64" height="63" fill="var(--lime)"/>
  <text class="swatch-label" x="1078" y="178">INSIDE</text>
  <text class="swatch-label" x="1078" y="194">SHELF</text>
  <text class="swatch-label" x="1078" y="210">COLOR</text>
</svg>
</body>
</html>
```